Gospel Music Tour Flyer

I would like to have created a 2 page landscape flyer that will highlight an upcoming gospel music tour. The tour will include gospel singers and orchestras across the US and Europe.
Please see attached "PowerPoint Example" for wording and concepts
Concepts Im Looking for on the First Page:
the First Page should be big and bold yet elegant and grab the attention of anyone. I've attached a File called "FlyerExample", this flyer is what I'm looking forward to on the first page. Big Picture but Elagant font. I love the back ground, but please note that my theme of this tour is called "silver rivers"…I would like for the flyer to also highlight an orchestra, since this tour is orchestrated based and will be promoted to orchestras. So pics of an orchestra seems to be a good idea
Concepts for the 2nd page.
I would just like it to be exciing to read and that the bullets of the tour is designed nicely. However, I'm open to your concepts.
The flyer will be used for print, Facebook, and instagram, the size should be landscape.
Updates
Good Morning All,
When desginig please avoid a black or dark background. Maybe something fall like or colorful and creative. Please make sure the fonts pop out and a orchestra is somehow embedded in the flyer. Feel free to be creative.
Thanks
Cole
Target Market(s)
Orchestra, conductors, gospel music lovers, classical musical lovers
Industry/Entity Type
Landscape
Look and feel
Each slider illustrates characteristics of the customer's brand and the style your logo design should communicate.

```html
<!DOCTYPE html>
<html lang="en">
<head>
<meta charset="utf-8">
<title>Silver Rivers – 2015 International Fall Gospel Music Tour</title>
<link rel="stylesheet" href="https://fonts.googleapis.com/css2?family=Cinzel:wght@400;700&display=swap">
<style>
  :root {
    --stage: #ececec;
    --fall-gold: #f0b25a;
    --fall-amber: #dc7f36;
    --fall-rust: #a9472a;
    --fall-wine: #7e2f2a;
    --brand: #fff1c9;
    --link: #ffe6a8;
    --text-light: #fffaf0;
    --text-soft: #fbe8cf;
    --accent-red: #6e0f12;
    --rule: rgba(255,240,210,.55);
  }
  * { box-sizing: border-box; margin: 0; padding: 0; }
  html, body { width: 1200px; height: 960px; overflow: hidden; }
  body {
    background: var(--stage);
    font-family: "Cinzel", serif;
    color: var(--text-light);
    position: relative;
  }
  .page {
    position: absolute;
    top: 262px;
    width: 560px;
    height: 436px;
    background: linear-gradient(180deg, var(--fall-gold) 0%, var(--fall-amber) 42%, var(--fall-rust) 78%, var(--fall-wine) 100%);
    box-shadow: 0 8px 24px rgba(0,0,0,.3);
    text-align: center;
    overflow: hidden;
    text-shadow: 0 1px 3px rgba(70,20,10,.55);
  }
  .page--details { left: 30px; }
  .page--cover { left: 610px; }

  .orchestra-backdrop {
    position: absolute; left: 0; right: 0; bottom: 0; width: 100%;
  }
  .page-content { position: relative; }

  .brand {
    display: inline-flex; align-items: center; gap: 8px;
    margin-top: 24px;
    color: var(--brand);
    font-weight: 700; font-size: 18px; letter-spacing: 1px;
  }
  .brand-dot { width: 10px; height: 10px; background: var(--brand); border-radius: 50%; }

  .tour-name { font-weight: 700; letter-spacing: 1px; }
  .tour-title { font-weight: 400; letter-spacing: .5px; }

  /* details page */
  .page--details .tour-name { margin-top: 22px; font-size: 24px; }
  .page--details .tour-title { font-size: 19px; }
  .book-today { color: var(--link); font-size: 17px; font-weight: 700; margin-top: 2px; }
  .includes {
    text-align: left;
    margin-top: 16px;
    padding: 10px 0 0 52px;
  }
  .includes-heading {
    font-size: 14px; font-weight: 700; text-decoration: underline; letter-spacing: .5px; margin-bottom: 8px;
  }
  .includes-list { list-style: none; }
  .includes-list li {
    font-size: 10px; line-height: 17px; letter-spacing: .3px; font-weight: 700;
    padding-left: 18px; position: relative;
  }
  .includes-list li::before {
    content: ""; position: absolute; left: 2px; top: 6px;
    width: 5px; height: 5px; background: var(--brand); transform: rotate(45deg);
  }
  .site-link { margin-top: 10px; color: var(--link); font-size: 9px; font-weight: 700; letter-spacing: .5px; }

  .partners {
    position: absolute; left: 120px; right: 120px; bottom: 14px;
    display: flex; justify-content: center; align-items: center; gap: 16px;
    padding-top: 10px; border-top: 1px solid var(--rule);
    text-shadow: none;
  }
  .partner { font-size: 9px; font-weight: 700; letter-spacing: .5px; }
  .partner--ministry { color: var(--brand); }
  .partner--label { background: #fff; color: #2a1408; padding: 3px 6px; }
  .partner--mark { color: var(--text-light); border: 1px solid var(--brand); padding: 3px 5px; }

  /* cover page */
  .page--cover .tour-title { margin-top: 16px; font-size: 20px; }
  .page--cover .tour-name { margin-top: 2px; font-size: 30px; }
  .lineup {
    display: flex; justify-content: space-between; align-items: flex-start;
    padding: 0 30px; margin-top: 14px;
  }
  .artist { width: 156px; }
  .artist-frame { height: 120px; display: flex; align-items: flex-end; justify-content: center; }
  .artist-photo { display: block; border-radius: 2px; box-shadow: 0 3px 8px rgba(60,15,5,.45); }
  .artist-name { font-size: 15px; font-weight: 700; margin-top: 10px; }
  .artist-role { font-size: 8px; font-weight: 700; color: var(--text-soft); line-height: 11px; margin-top: 4px; letter-spacing: .3px; }
  .artist-role .highlight { color: var(--accent-red); text-shadow: none; }
</style>
</head>
<body>

<section class="page page--details">
  <svg class="orchestra-backdrop" height="190" role="img" aria-label="Soft faded photo of a full orchestra on stage, string and brass sections">
    <defs><linearGradient id="orchA" x1="0" y1="0" x2="0" y2="1"><stop offset="0" stop-color="#7e2f2a" stop-opacity="0"/><stop offset="1" stop-color="#5a2218" stop-opacity=".55"/></linearGradient></defs>
    <rect width="100%" height="190" fill="url(#orchA)"/>
  </svg>
  <div class="page-content">
    <div class="brand"><span class="brand-dot"></span>Tender Oak Music Ministries</div>
    <h1 class="tour-name">“Silver Rivers”</h1>
    <h2 class="tour-title">2015 International Fall Gospel Music Tour</h2>
    <p class="book-today">“Book Today”</p>
    <div class="includes">
      <p class="includes-heading">Tour Includes:</p>
      <ul class="includes-list">
        <li>Orchestra Collaboration</li>
        <li>Sheet Music Provided</li>
        <li>Rhythms Section Provided</li>
        <li>6-9 Vocalist Provided or Choral Collaboration</li>
        <li>Choral Director, Cole Brown</li>
        <li>Guest Orchestra Director, from Venice, Italy “Marco Vellani”</li>
        <li>Pianist &amp; Hartwell Professor, Luca Ferranti (1-2 Song)</li>
        <li>1-2 Hours of Music Available</li>
      </ul>
    </div>
    <p class="site-link">www.tenderoakmusicministries.com</p>
  </div>
  <div class="partners">
    <span class="partner partner--ministry">Tender Oak</span>
    <span class="partner partner--label">Pairstone Music</span>
    <span class="partner partner--mark">Kestrel</span>
  </div>
</section>

<section class="page page--cover">
  <svg class="orchestra-backdrop" height="260" role="img" aria-label="Soft faded photo of a full orchestra performing on a warmly lit stage">
    <defs><linearGradient id="orchB" x1="0" y1="0" x2="0" y2="1"><stop offset="0" stop-color="#a9472a" stop-opacity="0"/><stop offset="1" stop-color="#5a2218" stop-opacity=".6"/></linearGradient></defs>
    <rect width="100%" height="260" fill="url(#orchB)"/>
  </svg>
  <div class="page-content">
    <div class="brand"><span class="brand-dot"></span>Tender Oak Music Ministries</div>
    <h2 class="tour-title">2015 International Fall Gospel Music Tour</h2>
    <h1 class="tour-name">“Silver Rivers”</h1>
    <div class="lineup">
      <div class="artist">
        <div class="artist-frame">
          <svg class="artist-photo" width="130" height="100" role="img" aria-label="Portrait photo of choral director Cole Brown">
            <defs><radialGradient id="photoA" cx="50%" cy="45%" r="60%"><stop offset="0" stop-color="#b98a68"/><stop offset="1" stop-color="#3a2218"/></radialGradient></defs>
            <rect width="130" height="100" fill="url(#photoA)"/>
          </svg>
        </div>
        <p class="artist-name">Cole Brown</p>
        <p class="artist-role">Award Winning<br>Choral Director</p>
      </div>
      <div class="artist">
        <div class="artist-frame">
          <svg class="artist-photo" width="150" height="118" role="img" aria-label="Photo of guest conductor Marco Vellani leading an orchestra">
            <defs><radialGradient id="photoB" cx="50%" cy="40%" r="65%"><stop offset="0" stop-color="#d49a62"/><stop offset=".6" stop-color="#6a3a28"/><stop offset="1" stop-color="#321a14"/></radialGradient></defs>
            <rect width="150" height="118" fill="url(#photoB)"/>
          </svg>
        </div>
        <p class="artist-name">Marco Vellani</p>
        <p class="artist-role">Special Guest Conductor<br>Venice, Italy</p>
      </div>
      <div class="artist">
        <div class="artist-frame">
          <svg class="artist-photo" width="130" height="108" role="img" aria-label="Photo of pianist Luca Ferranti seated at piano keys">
            <defs><linearGradient id="photoC" x1="0" y1="0" x2="1" y2="1"><stop offset="0" stop-color="#f2efe8"/><stop offset=".55" stop-color="#8a7a70"/><stop offset="1" stop-color="#2e2420"/></linearGradient></defs>
            <rect width="130" height="108" fill="url(#photoC)"/>
          </svg>
        </div>
        <p class="artist-name">Luca Ferranti</p>
        <p class="artist-role">Pianist &amp; Composer<br>Professor, The <span class="highlight">Hartwell</span> School<br>NYC</p>
      </div>
    </div>
  </div>
  <div class="partners">
    <span class="partner partner--ministry">Tender Oak</span>
    <span class="partner partner--label">Pairstone Music</span>
    <span class="partner partner--mark">Kestrel</span>
  </div>
</section>

</body>
</html>
```